Law Office needs stationery design and business card

I currently have been using the same letterhead for the last 8 years. Since i 'm about to adding another location, I want to revamp my letterhead and business card. I already have a logo i'm happy with. I will upload my current letterhead, fax sheet, envelope, and logos. I need a business card also. I have 2 locations, 1 phone number, 1 fax line, website, etc. If possible and fitting with the design, I would like to keep the same information listed currently on the letterhead.

**Keep in mind, I also NEED A FAX SHEET COVER. thank you
Updates

Hello, Please submit a Gray Scale or Black and White version of your designs also, since most of the time I will be printing NON color stationery. I will seldom use a color print for my letterhead, I would like to have a color version for my benefit, however i will print in grayscale majority of the time . For the Business Card, that can just be in color. When I get my business cards they will be in color.Thank youEnrique Added Sunday, September 18, 2016

Industry/Entity Type

Business

```html
<!DOCTYPE html>
<html lang="en">
<head>
<meta charset="utf-8">
<title>Marvell Law — Stationery System</title>
<link href="https://fonts.googleapis.com/css2?family=Cinzel:wght@500&family=Libre+Baskerville&family=Open+Sans:wght@400;600&display=swap" rel="stylesheet">
<style>
  :root{
    --backdrop:#d6d6d6;
    --paper:#ffffff;
    --ink:#1f1c1a;
    --gold:#bf9f62;
    --charcoal:#1d1a19;
    --rule-light:#9a9a9a;
    --mark-faint:#ececec;
  }
  *{box-sizing:border-box;margin:0;padding:0}
  html,body{width:900px;height:1200px;overflow:hidden;background:var(--backdrop)}
  body{position:relative;font-family:"Open Sans",Arial,sans-serif;color:var(--ink)}

  .suite{position:absolute;left:0;width:900px;height:600px}
  .suite--color{top:0;--accent:var(--gold)}
  .suite--mono{top:600px;--accent:var(--charcoal)}

  .sheet{position:absolute;background:var(--paper);box-shadow:0 1px 3px rgba(0,0,0,.18)}

  /* wordmark */
  .wordmark{display:flex;align-items:center;gap:5px;font-family:"Cinzel",serif;font-weight:500;color:var(--ink);white-space:nowrap;letter-spacing:.04em}
  .wordmark__square{display:block;background:var(--accent)}

  /* letterhead */
  .letterhead{left:148px;top:105px;width:284px;height:400px}
  .letterhead .wordmark{position:absolute;left:16px;top:32px;font-size:14px}
  .letterhead .wordmark__square{width:12px;height:12px}
  .letterhead__sender{position:absolute;right:17px;top:26px;text-align:right;font-family:"Libre Baskerville",serif;font-size:5.6px;line-height:7.2px}
  .letterhead__band{position:absolute;left:0;top:67px;width:157px;height:2.5px;background:var(--accent)}
  .letterhead__rule{position:absolute;left:157px;top:68.5px;width:66px;height:.6px;background:var(--rule-light)}
  .watermark{position:absolute;left:0;right:0;top:222px;display:flex;justify-content:center}
  .watermark .wordmark{position:static;color:var(--mark-faint);font-size:19px}
  .watermark .wordmark__square{width:16px;height:16px;background:var(--mark-faint)}
  .letterhead__footrule{position:absolute;left:12px;right:11px;top:358px;height:.6px;background:var(--accent)}
  .contact-block{text-align:center;font-size:4.1px;line-height:6.1px}
  .letterhead .contact-block{position:absolute;left:0;right:0;top:364px}

  /* business cards */
  .card{top:125px;width:137px;height:69px}
  .card--front{left:456px}
  .card--back{left:602px;overflow:hidden}
  .card__name{font-family:"Libre Baskerville",serif;font-size:4.9px;line-height:6px}
  .card__title{font-size:3.4px;font-style:italic;padding-left:10px}
  .card__tiny{font-size:2.7px;line-height:3.6px}
  .card--front .card__person{position:absolute;left:6px;top:31px}
  .card--front .card__person .card__tiny{margin-top:4px}
  .card__divider{position:absolute;left:63px;top:14px;width:.6px;height:42px;background:var(--rule-light)}
  .card--front .wordmark{position:absolute;left:72px;top:31px;font-size:7px;gap:3px}
  .card .wordmark__square{width:7px;height:7px}
  .card--front .card__offices{position:absolute;left:72px;top:44px}
  .card__web{position:absolute;right:6px;bottom:3px;font-size:2.6px}
  .card__panel{position:absolute;left:0;top:0;width:69px;height:69px;background:var(--accent);padding:14px 6px 0}
  .suite--mono .card__panel{color:#fff}
  .card__panel .card__tiny{margin-top:4px}
  .card--back .wordmark{position:absolute;left:75px;top:31px;font-size:6.3px;gap:3px}

  /* envelopes */
  .envelope{left:462px;width:288px;height:139px}
  .envelope--back{top:212px;overflow:hidden}
  .envelope--front{top:365px}
  .envelope__flap{position:absolute;left:0;top:0}
  .suite--mono .envelope__flap path{fill:#e4e4e4}
  .envelope--back .wordmark{position:absolute;left:0;right:0;top:76px;justify-content:center;font-size:7.5px;gap:3px}
  .envelope .wordmark__square{width:8px;height:8px}
  .envelope--back .contact-block{position:absolute;left:0;right:0;top:104px;font-size:3.6px;line-height:5.1px}
  .envelope__return{position:absolute;left:28px;top:100px;font-family:"Libre Baskerville",serif;font-size:5.6px;line-height:7.2px}
  .envelope--front .wordmark{position:absolute;right:18px;top:110px;font-size:10px}
  .envelope--front .wordmark__square{width:10px;height:10px}
</style>
</head>
<body>

<section class="suite suite--color" aria-label="Colour stationery">
  <article class="sheet letterhead">
    <div class="wordmark"><span class="wordmark__square"></span>MARVELL LAW</div>
    <address class="letterhead__sender">Tobias Marvell Esq.<br>48 Harbor Row<br>Suite 200<br>Linden, PA 19000<br>(555) 010.2468</address>
    <div class="letterhead__band"></div><div class="letterhead__rule"></div>
    <div class="watermark"><div class="wordmark"><span class="wordmark__square"></span>MARVELL LAW</div></div>
    <div class="letterhead__footrule"></div>
    <p class="contact-block">Office Locations * 48 Harbor Row, Suite 200, Linden, PA 19000 * 910 Ashby St, Fairvale, PA 19010<br>* phone 555.010.2468 * fax 555.010.3579 * www.MarvellLaw.com * FB "MarvellLaw"<br>Attorneys * Tobias Marvell Esq. * Nora Keller Esq. * Clara Dunn Esq. * Owen Hale Esq. <i>of counsel</i> *<br>Tobias@MarvellLaw.com * Nora@MarvellLaw.com * Clara@MarvellLaw.com * Owen@MarvellLaw.com</p>
  </article>

  <article class="sheet card card--front">
    <div class="card__person"><p class="card__name">Tobias Marvell Esq</p><p class="card__title">Attorney</p><p class="card__tiny">555.010.2468<br>tobias@marvelllaw.com</p></div>
    <div class="card__divider"></div>
    <div class="wordmark"><span class="wordmark__square"></span>MARVELL LAW</div>
    <p class="card__offices card__tiny"><b>Office Locations</b><br>* 48 Harbor Row, Suite 200, Linden, PA<br>* 910 Ashby St, Fairvale, PA<br>Phone 555.010.2468<br>Fax 555.010.3579</p>
    <p class="card__web">www.MarvellLaw.com</p>
  </article>
  <article class="sheet card card--back">
    <div class="card__panel"><p class="card__name">Tobias Marvell Esq</p><p class="card__title">Attorney</p><p class="card__tiny">555.010.2468<br>tobias@marvelllaw.com</p><p class="card__tiny"><b>Office Locations</b><br>* 48 Harbor Row, Linden, PA<br>* 910 Ashby St, Fairvale, PA<br>Fax 555.010.3579</p></div>
    <div class="wordmark"><span class="wordmark__square"></span>MARVELL LAW</div>
  </article>

  <article class="sheet envelope envelope--back">
    <svg class="envelope__flap" width="288" height="42" viewBox="0 0 288 42"><path d="M0 0H288V4Q288 36 270 38H18Q4 36 0 4Z" fill="var(--gold)"/></svg>
    <div class="wordmark"><span class="wordmark__square"></span>MARVELL LAW</div>
    <p class="contact-block">Office Locations * 48 Harbor Row, Suite 200, Linden, PA 19000 * 910 Ashby St, Fairvale, PA 19010<br>* phone 555.010.2468 * fax 555.010.3579 * www.MarvellLaw.com * FB "MarvellLaw"<br>Attorneys * Tobias Marvell Esq. * Nora Keller Esq. * Clara Dunn Esq. * Owen Hale Esq. <i>of counsel</i> *<br>Tobias@MarvellLaw.com * Nora@MarvellLaw.com * Clara@MarvellLaw.com * Owen@MarvellLaw.com</p>
  </article>
  <article class="sheet envelope envelope--front">
    <address class="envelope__return">Tobias Marvell Esq.<br>77 Sample Lane Apt<br>D Linden, PA 19000</address>
    <div class="wordmark"><span class="wordmark__square"></span>MARVELL LAW</div>
  </article>
</section>

<section class="suite suite--mono" aria-label="Grayscale stationery">
  <article class="sheet letterhead">
    <div class="wordmark"><span class="wordmark__square"></span>MARVELL LAW</div>
    <address class="letterhead__sender">Tobias Marvell Esq.<br>48 Harbor Row<br>Suite 200<br>Linden, PA 19000<br>(555) 010.2468</address>
    <div class="letterhead__band"></div><div class="letterhead__rule"></div>
    <div class="watermark"><div class="wordmark"><span class="wordmark__square"></span>MARVELL LAW</div></div>
    <div class="letterhead__footrule" style="background:var(--rule-light)"></div>
    <p class="contact-block">Office Locations * 48 Harbor Row, Suite 200, Linden, PA 19000 * 910 Ashby St, Fairvale, PA 19010<br>* phone 555.010.2468 * fax 555.010.3579 * www.MarvellLaw.com * FB "MarvellLaw"<br>Attorneys * Tobias Marvell Esq. * Nora Keller Esq. * Clara Dunn Esq. * Owen Hale Esq. <i>of counsel</i> *<br>Tobias@MarvellLaw.com * Nora@MarvellLaw.com * Clara@MarvellLaw.com * Owen@MarvellLaw.com</p>
  </article>

  <article class="sheet card card--front">
    <div class="card__person"><p class="card__name">Tobias Marvell Esq</p><p class="card__title">Attorney</p><p class="card__tiny">555.010.2468<br>tobias@marvelllaw.com</p></div>
    <div class="card__divider"></div>
    <div class="wordmark"><span class="wordmark__square"></span>MARVELL LAW</div>
    <p class="card__offices card__tiny"><b>Office Locations</b><br>* 48 Harbor Row, Suite 200, Linden, PA<br>* 910 Ashby St, Fairvale, PA<br>Phone 555.010.2468<br>Fax 555.010.3579</p>
    <p class="card__web">www.MarvellLaw.com</p>
  </article>
  <article class="sheet card card--back">
    <div class="card__panel"><p class="card__name">Tobias Marvell Esq</p><p class="card__title">Attorney</p><p class="card__tiny">555.010.2468<br>tobias@marvelllaw.com</p><p class="card__tiny"><b>Office Locations</b><br>* 48 Harbor Row, Linden, PA<br>* 910 Ashby St, Fairvale, PA<br>Fax 555.010.3579</p></div>
    <div class="wordmark"><span class="wordmark__square"></span>MARVELL LAW</div>
    <p class="card__web">www.MarvellLaw.com</p>
  </article>

  <article class="sheet envelope envelope--back">
    <svg class="envelope__flap" width="288" height="42" viewBox="0 0 288 42"><path d="M0 0H288V4Q288 36 270 38H18Q4 36 0 4Z"/></svg>
    <div class="wordmark"><span class="wordmark__square"></span>MARVELL LAW</div>
    <p class="contact-block">Office Locations * 48 Harbor Row, Suite 200, Linden, PA 19000 * 910 Ashby St, Fairvale, PA 19010<br>* phone 555.010.2468 * fax 555.010.3579 * www.MarvellLaw.com * FB "MarvellLaw"<br>Attorneys * Tobias Marvell Esq. * Nora Keller Esq. * Clara Dunn Esq. * Owen Hale Esq. <i>of counsel</i> *<br>Tobias@MarvellLaw.com * Nora@MarvellLaw.com * Clara@MarvellLaw.com * Owen@MarvellLaw.com</p>
  </article>
  <article class="sheet envelope envelope--front">
    <address class="envelope__return">Tobias Marvell Esq.<br>77 Sample Lane Apt<br>D Linden, PA 19000</address>
    <div class="wordmark"><span class="wordmark__square"></span>MARVELL LAW</div>
  </article>
</section>

</body>
</html>
```